1923 Basins & Spouts Business Card

I'm wanting to get a business card designed. Our business is 1923 Basins & Spouts
Details for the card:

1923 Basins & Spouts
Name: Gareth Vostle
Email: gareth@1923basinsandspouts.com.au
Website: www.1923basinsandspouts.com.au
Mobile: 0439 602 158
Phone: 02 5550 1843

Font of Basins & Spouts is called Snell Roundhand. Not sue what font logo text is.

I'm thinking two sided but it doesn't have to be.

```html
<!DOCTYPE html>
<html lang="en">
<head>
<meta charset="UTF-8">
<title>1923 Basins &amp; Spouts – Business Card</title>
<link rel="stylesheet" href="https://fonts.googleapis.com/css2?family=Open+Sans:wght@400;600;700&display=swap">
<style>
  :root {
    --backdrop: #e9e7e3;
    --card-white: #ffffff;
    --card-black: #0b0b0b;
    --ink: #161616;
    --rule: #9a9a9a;
    --frame: #cfcfcf;
    --ink-light: #e6e6e6;
  }
  * { margin: 0; padding: 0; box-sizing: border-box; }
  html, body {
    width: 1200px; height: 720px; overflow: hidden;
    background: var(--backdrop);
    font-family: "Open Sans", Arial, sans-serif;
  }
  .canvas {
    position: relative; width: 1200px; height: 720px;
    display: flex; align-items: center; justify-content: center; gap: 48px;
  }
  .card {
    position: relative; width: 520px; height: 300px;
    box-shadow: 0 10px 26px rgba(0,0,0,0.18);
    overflow: hidden;
  }
  /* Front */
  .card--front { background: var(--card-white); color: var(--ink); }
  .brand {
    position: absolute; left: 0; top: 0; width: 215px; height: 300px;
    display: flex; flex-direction: column; align-items: center; justify-content: center;
  }
  .brand__row { display: flex; align-items: center; gap: 10px; }
  .brand__dot {
    width: 26px; height: 26px; border-radius: 50%;
    background: var(--ink); flex: none;
  }
  .brand__name {
    font-weight: 600; font-size: 19px; line-height: 1.15; color: var(--ink);
  }
  .brand__tagline {
    margin-top: 14px; font-size: 7.6px; color: var(--ink); white-space: nowrap;
  }
  .divider {
    position: absolute; left: 215px; top: 72px; width: 1px; height: 172px;
    background: var(--rule);
  }
  .name-band {
    position: absolute; left: 226px; right: 0; top: 42px; height: 40px;
    background: var(--card-black); color: #fff;
    display: flex; align-items: center; padding-left: 12px; gap: 9px;
  }
  .name-band__icon { width: 20px; height: 20px; flex: none; }
  .name-band__name { font-size: 11.5px; font-weight: 700; letter-spacing: 0.3px; line-height: 1.1; }
  .name-band__role { font-size: 8px; letter-spacing: 0.4px; line-height: 1.2; }
  .contacts {
    position: absolute; left: 238px; top: 100px; list-style: none;
    display: flex; flex-direction: column; gap: 10px;
  }
  .contacts__item { display: flex; align-items: center; gap: 9px; font-size: 11.5px; color: var(--ink); white-space: nowrap; }
  .contacts__icon { width: 16px; height: 16px; flex: none; }
  .contacts__lines { line-height: 1.3; }
  /* Back */
  .card--back { background: var(--card-black); color: #fff; }
  .card__frame {
    position: absolute; inset: 16px; border: 1px solid var(--frame);
  }
  .back-brand {
    position: absolute; left: 0; right: 0; top: 96px;
    display: flex; flex-direction: column; align-items: center;
  }
  .back-brand__row { display: flex; align-items: center; gap: 12px; }
  .back-brand__dot { width: 34px; height: 34px; border-radius: 50%; background: #fff; flex: none; }
  .back-brand__name { font-weight: 600; font-size: 26px; color: #fff; white-space: nowrap; }
  .back-brand__tagline { margin-top: 10px; font-size: 9px; color: var(--ink-light); white-space: nowrap; }
  .back-web {
    position: absolute; left: 0; right: 0; top: 196px; text-align: center;
    font-size: 9px; color: var(--ink-light); letter-spacing: 0.2px;
  }
</style>
</head>
<body>
<main class="canvas">
  <section class="card card--front" aria-label="Card front">
    <div class="brand">
      <div class="brand__row">
        <span class="brand__dot"></span>
        <span class="brand__name">1923<br>Basins &amp; Spouts</span>
      </div>
      <p class="brand__tagline">Blending classic charm with lasting everyday function</p>
    </div>
    <span class="divider"></span>
    <div class="name-band">
      <svg class="name-band__icon" viewBox="0 0 20 20" aria-hidden="true">
        <circle cx="10" cy="10" r="9" fill="none" stroke="#fff" stroke-width="1.2"/>
        <circle cx="10" cy="8" r="3.2" fill="#fff"/>
        <path d="M4.6 15.6c1.2-2.6 3.2-3.8 5.4-3.8s4.2 1.2 5.4 3.8" fill="#fff"/>
      </svg>
      <div>
        <p class="name-band__name">GARETH VOSTLE</p>
        <p class="name-band__role">DESIGNATION</p>
      </div>
    </div>
    <ul class="contacts">
      <li class="contacts__item">
        <svg class="contacts__icon" viewBox="0 0 16 16" aria-hidden="true">
          <circle cx="8" cy="8" r="7.3" fill="none" stroke="#161616" stroke-width="1.2"/>
          <path d="M5.3 4.4l1.4-.3.8 1.9-.9.7c.5 1.1 1.3 1.9 2.4 2.4l.7-.9 1.9.8-.3 1.4c-3.3.2-6.2-2.7-6-6z" fill="#161616"/>
        </svg>
        <span class="contacts__lines">02 5550 1843<br>0439 602 158</span>
      </li>
      <li class="contacts__item">
        <svg class="contacts__icon" viewBox="0 0 16 16" aria-hidden="true">
          <circle cx="8" cy="8" r="7.3" fill="#161616"/>
          <ellipse cx="8" cy="8" rx="3" ry="7.3" fill="none" stroke="#fff" stroke-width="0.9"/>
          <path d="M0.8 8h14.4M2 4.6h12M2 11.4h12" stroke="#fff" stroke-width="0.9"/>
        </svg>
        <span>www.1923basinsandspouts.com.au</span>
      </li>
      <li class="contacts__item">
        <svg class="contacts__icon" viewBox="0 0 16 16" aria-hidden="true">
          <rect x="0.8" y="3" width="14.4" height="10" fill="#161616"/>
          <path d="M1.6 3.8L8 9l6.4-5.2" fill="none" stroke="#fff" stroke-width="1.1"/>
        </svg>
        <span>gareth@1923basinsandspouts.com.au</span>
      </li>
    </ul>
  </section>

  <section class="card card--back" aria-label="Card back">
    <span class="card__frame"></span>
    <div class="back-brand">
      <div class="back-brand__row">
        <span class="back-brand__dot"></span>
        <span class="back-brand__name">1923 Basins &amp; Spouts</span>
      </div>
      <p class="back-brand__tagline">Blending classic charm with lasting everyday function</p>
    </div>
    <p class="back-web">www.1923basinsandspouts.com.au</p>
  </section>
</main>
</body>
</html>
```